Brindale Community Education Poster

We need a poster that attracts people to come and do classes at our community education program, "Brindale Community Education". Our website is www.brindalecommunityed.example.

We run affordably priced classes that are designed to meet the evolving educational preferences of our local community.

Our target market are well educated, creative, well travelled, middle to high income and 35 - 60 (middle aged, active adult).

Each term (the Australian school year is divided into 4 x 10 week terms) we offer Tablet for beginners, Creative writing courses, Art Classes, Literary appreciation classes, Couples Dance Classes, Tai Chi, Yoga, Qigong and Language classes.

We are a not-for-profit organisation that is run by the Families & Residents Guild. All the proceeds from and all our proceeds go the children of Brindale State School.

This poster will be hung in libraries, on community noticeboards, and at events.

We would like to see designs that use our school colours - maroon and blue (please see logo and photo)

Target Market(s)

Our target market are well educated, aged 35-60, who aspire to be, or are, life long learners and/or active older adults. Community minded.

Industry/Entity Type

Education

Requirements
Must have
• Must be able to use design for both A4 and A3 poster sizes.

```html
<!DOCTYPE html>
<html lang="en">
<head>
<meta charset="utf-8">
<title>Brindale Community Education</title>
<link rel="stylesheet" href="https://fonts.googleapis.com/css2?family=Oswald:wght@500&family=Source+Sans+3:wght@400;600;700&display=swap">
<style>
  :root {
    --maroon: #7a1a3b;
    --border-tone: #a0566b;
    --cream: #e9dcc5;
    --blue: #3a88c8;
    --blue-dark: #27679c;
    --white: #ffffff;
    --photo-tone-a: #c9b8a6;
    --photo-tone-b: #6f7f79;
  }
  * { box-sizing: border-box; margin: 0; padding: 0; }
  html, body { width: 1079px; height: 1200px; overflow: hidden; background: var(--white); }
  .canvas { position: relative; width: 1079px; height: 1200px; }
  .poster {
    position: absolute; left: 46px; top: 51px; width: 736px; height: 1119px;
    background: var(--cream); border: 27px solid var(--border-tone);
  }
  .ribbon { position: absolute; left: 0; top: 0; width: 1079px; height: 1200px; pointer-events: none; }
  .title {
    position: absolute; left: 159px; top: 129px; width: 510px; height: 61px;
    display: flex; align-items: center; justify-content: center;
    font-family: "Oswald", sans-serif; font-weight: 500; font-size: 41px;
    color: var(--white); white-space: nowrap;
  }
  .photo-frame {
    position: absolute; left: 91px; top: 241px; width: 648px; height: 434px;
    background: var(--white); padding: 7px;
  }
  .photo {
    width: 100%; height: 100%;
    background: linear-gradient(110deg, #e6e4e2 0%, var(--photo-tone-a) 40%, #d8c2ad 70%, var(--photo-tone-b) 100%);
  }
  .text { font-family: "Source Sans 3", sans-serif; color: var(--maroon); }
  .intro {
    position: absolute; left: 91px; top: 706px; width: 680px;
    font-size: 24.5px; line-height: 20px; white-space: nowrap;
  }
  .offer-heading {
    position: absolute; left: 91px; top: 780px;
    font-family: "Source Sans 3", sans-serif; font-weight: 700; font-size: 23px;
    color: var(--blue); letter-spacing: 0.6px;
  }
  .offer-list {
    position: absolute; left: 91px; top: 815px; list-style: none;
    font-size: 25px; line-height: 24.6px;
  }
  .offer-list li::before { content: "· "; }
  .school-mark {
    position: absolute; left: 515px; top: 785px; width: 222px;
    display: flex; flex-direction: column; align-items: center; gap: 16px;
  }
  .school-mark .dot { width: 130px; height: 130px; border-radius: 50%; background: var(--blue); }
  .school-mark .name {
    font-family: "Source Sans 3", sans-serif; font-weight: 700; font-size: 24px;
    color: var(--maroon); text-align: center; line-height: 26px;
  }
  .contact {
    position: absolute; left: 91px; top: 1066px; width: 648px; text-align: center;
    font-weight: 600; font-size: 14.5px; line-height: 17.5px;
  }
</style>
</head>
<body>
<div class="canvas">
  <div class="poster"></div>

  <svg class="ribbon" viewBox="0 0 1079 1200" aria-hidden="true">
    <polygon points="70,140 204,140 204,205 70,205 128,172" fill="var(--blue-dark)"/>
    <polygon points="669,140 758,140 702,172 758,205 669,205" fill="var(--blue-dark)"/>
    <polygon points="159,190 204,190 204,205" fill="#111"/>
    <polygon points="669,190 626,190 626,205" fill="#111"/>
    <rect x="159" y="129" width="510" height="61" fill="var(--blue)"/>
  </svg>
  <div class="title">Brindale Community Education</div>

  <div class="photo-frame">
    <div class="photo" role="img" aria-label="Photo of four smiling school children standing in a row in a classroom"></div>
  </div>

  <p class="text intro">We run affordably priced classes that are designed to meet the<br>evolving educational preferences of our local community.</p>

  <h2 class="offer-heading">WE OFFER:</h2>
  <ul class="text offer-list">
    <li>Tablet for beginners</li>
    <li>Creative writing courses</li>
    <li>Art Classes</li>
    <li>Literary appreciation classes</li>
    <li>Couples Dance Classes</li>
    <li>Tai Chi</li>
    <li>Yoga</li>
    <li>Qigong</li>
    <li>Language classes</li>
  </ul>

  <div class="school-mark">
    <span class="dot"></span>
    <span class="name">Brindale State School</span>
  </div>

  <div class="text contact">
    <p>CONTACT INFORMATION:</p>
    <p>Telephone: (07) 5550 2444 | Facsimile: (07) 5550 2400</p>
    <p>Email: office@brindaless.example &nbsp;|www.brindaless.example</p>
    <p>18 Wattle Rd Brindale Qld 4000</p>
  </div>
</div>
</body>
</html>
```